Modern Web Design for Nonprofit Organization

Our client is looking to redesign their website. They want a modern look, clean and professional, that integrates their new brand guidelines.

Here is clients current site:
http://www.valorandes.org/

They want their own unique design but here are some sites the clients likes:
https://www.brixtonvane.com/en/
https://oakhollowrise.org/
https://www.lumacraft.com/
https://www.tbnlawgroup.com/
https://www.greyharborco.org/

Attached please find the clients logos, color palette, site plan and design specs.

You will create a homepage mockup that will have the following sections in this order:
1. Thin Alert Bar at very top with one line message
2. Nav Bar with Logo and Main Nav (red in site plan)
3. Hero Image or Video
4. Signup Bar with name email and zip and connect button
5. Intro section with image, welcome message, and supporter counter
6. Featured Action section with call to action
7. Event section with two upcoming event cards
8. Latest News section with three latest blog post
9. Support our work (donation) section
10. Worker and Member Stories Section with feed of social posts
11. Footer.

You can use text and images from clients existing site or placeholder images and placeholder text.

Please submit as many home page mockups/idea boards as you like. Client will pick the top three and ask for some revisions. If you are selected this will lead to a lot of work for this client.

Project is private please adhere to ArtPlenary terms of use and do not share any materials please.

QUICKEST RESPONSE PLEASE!

Thanks for looking!

Target Market(s)

Non profit donors and farmworker advocates

Number of Pages Required

2 page

Font styles to use
Sans Serif

Requirements
Must have
• Adhere to brief and client brand ID
Nice to have
• World class design

```html
<!DOCTYPE html>
<html lang="en">
<head>
<meta charset="utf-8">
<title>Fieldline Foundation – Home</title>
<link href="https://fonts.googleapis.com/css2?family=Fira+Sans+Condensed:wght@400;500;600;700&family=Fira+Sans+Extra+Condensed:wght@300;500;600;700&display=swap" rel="stylesheet">
<style>
:root{
  --red:#d80f0f;
  --yellow:#fbc900;
  --teal:#0f9aa0;
  --ink:#111111;
  --muted:#333333;
  --white:#ffffff;
  --footer:#050505;
  --leaf:#3f6a24;
  --leaf-dark:#1e3414;
  --leaf-light:#7fa84a;
  --straw:#c49a5e;
  --denim:#5f7fa6;
  --soil:#8d8676;
  --head:"Fira Sans Extra Condensed", sans-serif;
  --body:"Fira Sans Condensed", sans-serif;
}
*{box-sizing:border-box;margin:0;padding:0}
html,body{width:1200px;height:3413px;overflow:hidden}
body{position:relative;background:var(--white);font-family:var(--body);color:var(--ink)}
.abs{position:absolute}
.btn{display:inline-flex;align-items:center;justify-content:center;background:var(--yellow);color:var(--ink);font-family:var(--body);font-weight:600;font-size:9px;letter-spacing:.2px;border-radius:15px;text-transform:uppercase}

/* alert */
.alert-bar{top:0;left:0;width:1200px;height:36px;background:var(--red);color:var(--white);font-size:10px;letter-spacing:.6px;display:flex;align-items:center;justify-content:center}

/* nav */
.nav-bar{top:36px;left:0;width:1200px;height:61px;background:var(--white)}
.brand{left:113px;top:10px;display:flex;align-items:center;gap:8px}
.brand-mark{width:40px;height:40px;border-radius:50%;background:var(--red)}
.brand-name{font-family:var(--body);font-weight:700;font-size:14px;line-height:14px;color:var(--ink);text-transform:uppercase}
.main-nav{left:441px;top:0;height:61px;display:flex;align-items:center}
.main-nav a{font-size:9.5px;font-weight:500;color:var(--ink);text-decoration:none;text-transform:uppercase;margin-right:42px}
.main-nav a.active{color:var(--red)}
.nav-donate{left:1013px;top:17px;width:74px;height:29px}

/* photo placeholders: soft gradients in the scene's own tones */
.photo-field{
  background:
    radial-gradient(ellipse 18% 12% at 40% 12%, rgba(196,154,94,.75), transparent 70%),
    radial-gradient(ellipse 22% 30% at 38% 42%, rgba(95,127,166,.55), transparent 70%),
    radial-gradient(ellipse 14% 10% at 70% 8%, rgba(196,154,94,.55), transparent 70%),
    radial-gradient(ellipse 40% 40% at 85% 70%, rgba(127,168,74,.55), transparent 70%),
    radial-gradient(ellipse 45% 35% at 15% 85%, rgba(30,52,20,.8), transparent 70%),
    linear-gradient(160deg,#55783a 0%,#3b6024 45%,#22391a 100%);
}
.photo-farmer{
  background:
    radial-gradient(ellipse 30% 16% at 50% 22%, rgba(176,132,78,.95), transparent 72%),
    radial-gradient(ellipse 14% 12% at 50% 38%, rgba(190,140,100,.9), transparent 72%),
    radial-gradient(ellipse 30% 22% at 50% 62%, rgba(95,127,166,.8), transparent 72%),
    radial-gradient(ellipse 36% 14% at 50% 84%, rgba(190,170,70,.9), transparent 72%),
    radial-gradient(ellipse 40% 50% at 12% 30%, rgba(160,190,90,.7), transparent 72%),
    radial-gradient(ellipse 40% 50% at 88% 30%, rgba(140,175,80,.6), transparent 72%),
    linear-gradient(170deg,#6f9440 0%,#3f6a24 70%,#2e4f1c 100%);
}
.photo-standing{
  background:
    radial-gradient(ellipse 14% 40% at 20% 30%, rgba(70,90,120,.85), transparent 72%),
    radial-gradient(ellipse 14% 40% at 50% 25%, rgba(80,100,130,.85), transparent 72%),
    radial-gradient(ellipse 14% 40% at 80% 30%, rgba(70,90,120,.8), transparent 72%),
    linear-gradient(180deg,#5b6c80 0%,#7c8590 50%,#b3ab9b 75%,#cfc6b4 100%);
}
.photo-rows{
  background:
    linear-gradient(180deg,#7fb4e6 0%,#a8cdee 32%,#5f9a3a 36%,#3c7426 70%,#2b5b1c 100%);
}
.photo-crop{
  background:
    radial-gradient(ellipse 40% 30% at 30% 30%, rgba(150,190,90,.7), transparent 72%),
    radial-gradient(ellipse 40% 30% at 75% 70%, rgba(30,60,20,.6), transparent 72%),
    linear-gradient(160deg,#5a9233,#2d5b1d);
}

/* hero */
.hero{top:97px;left:0;width:1200px;height:600px}
.hero::after{content:"";position:absolute;inset:0;background:linear-gradient(90deg,rgba(0,0,0,.35),rgba(0,0,0,.05))}
.hero > *{z-index:1}
.hero-title{left:113px;top:188px;font-family:var(--head);font-weight:700;font-size:76px;line-height:66px;color:var(--white)}
.hero-sub{left:113px;top:346px;font-family:var(--head);font-weight:600;font-size:19px;color:#e6e6e6}
.signup{left:113px;top:384px;width:262px;height:28px;background:var(--white);border-radius:14px;display:flex;align-items:center;justify-content:space-between}
.signup span{font-size:9.5px;padding-left:15px;color:var(--ink)}
.signup .btn{width:74px;height:28px;border-radius:14px;padding-left:0}

/* intro */
.intro-photo{left:113px;top:772px;width:483px;height:483px;border-radius:50%}
.welcome-title{left:675px;top:850px;font-family:var(--head);font-weight:700;font-size:46px;color:var(--ink)}
.welcome-text{left:675px;top:918px;width:418px;font-size:10.8px;line-height:22.5px;color:var(--muted)}
.stats{left:675px;top:1108px;width:412px;height:60px;display:flex}
.stat{flex:1;display:flex;flex-direction:column;justify-content:center;text-align:center}
.stat:first-child{text-align:left;padding-left:8px}
.stat:last-child{text-align:right}
.stat + .stat{border-left:1.5px solid #555}
.stat b{font-family:var(--head);font-weight:600;font-size:19px;color:var(--ink)}
.stat span{font-family:var(--head);font-weight:500;font-size:14px;color:var(--red);text-transform:uppercase}

/* featured actions */
.section-title{left:0;width:1200px;text-align:center;font-family:var(--head);font-weight:600;font-size:23px;text-transform:uppercase}
.actions{left:113px;top:1385px;display:flex;gap:28px}
.action-card{width:173px;height:301px;border:1px solid #d8d8d8;box-shadow:0 1px 4px rgba(0,0,0,.12);display:flex;flex-direction:column;align-items:center;padding-top:30px;background:var(--white)}
.action-card svg{width:78px;height:78px}
.action-card h3{font-family:var(--head);font-weight:600;font-size:20px;line-height:22px;color:var(--red);text-align:center;height:50px;display:flex;align-items:center;margin-top:2px}
.action-card p{font-size:8.5px;line-height:15px;text-transform:uppercase;text-align:center;color:var(--muted);width:104px;margin-top:6px}
.action-card .btn{width:75px;height:28px;margin-top:18px;font-size:8.5px}

/* events */
.events{top:1762px;left:0;width:1200px;height:373px;
  background:
    radial-gradient(ellipse 60% 20% at 50% 12%, rgba(120,140,110,.45), transparent 72%),
    linear-gradient(180deg,#3e4a3a 0%,#2c3b25 40%,#23321c 70%,#1a2315 100%)}
.events .section-title{top:83px;color:var(--white)}
.event-card{top:147px;width:480px;height:149px;border:1px solid var(--teal);display:flex}
.event-date{width:150px;height:100%;background:var(--teal);color:var(--white);display:flex;flex-direction:column;align-items:center;justify-content:center}
.event-date b{font-family:var(--head);font-weight:300;font-size:64px;line-height:58px}
.event-date span{font-size:11px;font-weight:600}
.event-body{padding:20px 16px;color:var(--white)}
.event-body h4{font-family:var(--head);font-weight:600;font-size:15px;text-transform:uppercase}
.event-body p{font-size:10.5px;line-height:13.5px;margin-top:10px;width:265px}
.attend{display:flex;align-items:center;gap:7px;margin-top:12px;font-size:10px}

/* news */
.news{left:113px;top:2266px;display:flex;gap:15px}
.news-item{width:315px;height:207px}
.news-feature{background:
    radial-gradient(ellipse 30% 25% at 50% 75%, rgba(255,110,40,.5), transparent 72%),
    linear-gradient(160deg,#dc2a10 0%,#c4160a 100%);padding:50px 38px;color:var(--white)}
.news-feature h4{font-family:var(--head);font-weight:600;font-size:19px;line-height:22px}
.news-feature a{display:inline-block;margin-top:6px;font-size:10px;font-weight:600;color:var(--white)}

/* support */
.support{top:2548px;left:0;width:1200px;height:224px}
.support::after{content:"";position:absolute;inset:0;background:rgba(30,32,34,.45)}
.support > *{z-index:1}
.support .section-title{top:74px;color:var(--white)}
.support .btn{left:563px;top:119px;width:74px;height:28px}

/* stories */
.stories-title{left:113px;top:2842px;font-family:var(--head);font-weight:600;font-size:23px;text-transform:uppercase}
.quote-mark{left:113px;top:2898px;font-family:var(--head);font-weight:700;font-size:40px;color:var(--ink)}
.story-text{left:132px;top:2928px;width:462px;font-size:10.8px;line-height:26.4px;color:var(--muted)}
.story-author{left:400px;width:193px;top:3132px;text-align:right;font-family:var(--head);font-weight:600;font-size:19px}
.arrows{left:113px;top:3204px;display:flex;gap:17px}
.arrow{width:21px;height:21px;border-radius:50%;background:var(--yellow);display:flex;align-items:center;justify-content:center}
.feed{left:650px;top:2834px;width:436px;height:436px;display:grid;grid-template-columns:repeat(4,1fr);grid-template-rows:repeat(4,1fr);gap:6px}
.feed .big{grid-column:span 2;grid-row:span 2}

/* footer */
.footer{top:3346px;left:0;width:1200px;height:67px;background:var(--footer);display:flex;align-items:center;justify-content:center;gap:46px}
.footer a{color:var(--white);text-decoration:none;font-size:11.5px;font-weight:600}
.social{display:flex;gap:14px;margin-left:-10px}
.social span{width:22px;height:22px;border-radius:50%}
</style>
</head>
<body>

<div class="abs alert-bar">Alert! Covid-19 is still present. Wear Mask, &nbsp;Santize, Protect yourself and everyone around &nbsp;you!</div>

<header class="abs nav-bar">
  <div class="abs brand"><span class="brand-mark"></span><span class="brand-name">Fieldline<br>Foundation</span></div>
  <nav class="abs main-nav">
    <a class="active" href="#">Home</a><a href="#">Get Help Now</a><a href="#">Take Action</a><a href="#">News and Events</a><a href="#">Support Our Work</a><a href="#">About Us</a>
  </nav>
  <span class="abs btn nav-donate">Donate</span>
</header>

<section class="abs hero photo-field" role="img" aria-label="Farmworkers in wide-brimmed hats harvesting leafy greens in a field">
  <h1 class="abs hero-title">Join the<br>Farm Worker Movement</h1>
  <p class="abs hero-sub">Sign up and Stay Informed</p>
  <div class="abs signup"><span>Your Email</span><span class="btn">Submit</span></div>
</section>

<div class="abs intro-photo photo-farmer" role="img" aria-label="Smiling farmworker holding a wooden tray of freshly picked cacao pods"></div>
<h2 class="abs welcome-title">Welcome!</h2>
<p class="abs welcome-text">The Fieldline Foundation is a dynamic nonprofit organization established in 2006. The Fieldline Foundation’s core purpose is to empower communities to ensure human dignity. We serve over 90,000 immigrants annually through a holistic approach; we provide critical services and engage our constituents in systemic change to break the cycle of poverty. Our regional offices are safe havens that provide resources and services—such as credible immigration legal advice—and act as hubs for educational outreach and organizing.</p>
<div class="abs stats">
  <div class="stat"><b>10, 000</b><span>Supporters</span></div>
  <div class="stat"><b>5, 000</b><span>Volunteers</span></div>
  <div class="stat"><b>$15, 000</b><span>Donations</span></div>
</div>

<h2 class="abs section-title" style="top:1325px">Featured Actions</h2>
<div class="abs actions">
  <div class="action-card">
    <svg viewBox="0 0 78 78" fill="none" stroke="#d80f0f" stroke-width="2.6" stroke-linecap="round" stroke-linejoin="round"><path d="M24 24h30M29 24l2-12h16l2 12"/><path d="M29 26c0 9 4 15 10 15s10-6 10-15"/><path d="M16 74V58c0-8 10-13 23-13s23 5 23 13v16z"/><path d="M30 47v27M48 47v27M30 60h18"/></svg>
    <h3>Farmworker<br>Legalization</h3>
    <p>Lorem ipsum dolor sit amet, consectetur adipiscing elit, sed do</p>
    <span class="btn">Read More</span>
  </div>
  <div class="action-card">
    <svg viewBox="0 0 78 78" fill="none" stroke="#d80f0f" stroke-width="2.6" stroke-linecap="round"><circle cx="39" cy="39" r="15"/><path d="M39 6v10M39 62v10M6 39h10M62 39h10M16 16l7 7M55 55l7 7M62 16l-7 7M23 55l-7 7"/></svg>
    <h3>Heat</h3>
    <p>Lorem ipsum dolor sit amet, consectetur adipiscing elit, sed do</p>
    <span class="btn">Read More</span>
  </div>
  <div class="action-card">
    <svg viewBox="0 0 78 78" fill="none" stroke="#d80f0f" stroke-width="2.6" stroke-linecap="round" stroke-linejoin="round"><path d="M27 30h22v40a3 3 0 0 1-3 3H30a3 3 0 0 1-3-3z"/><path d="M32 30v-8h12v8M34 22V12h18l6 4M52 12v5"/><circle cx="38" cy="51" r="8"/><path d="M33 46l10 10"/></svg>
    <h3>Pesticides</h3>
    <p>Lorem ipsum dolor sit amet, consectetur adipiscing elit, sed do</p>
    <span class="btn">Read More</span>
  </div>
  <div class="action-card">
    <svg viewBox="0 0 78 78" fill="none" stroke="#d80f0f" stroke-width="2.6" stroke-linecap="round" stroke-linejoin="round"><path d="M20 52c-9 0-13-10-7-16-4-8 4-16 12-13 3-9 15-10 20-3 8-4 17 3 14 11 8 3 7 16-2 17-2 6-10 8-15 4-5 5-15 4-18-2-2 1-3 2-4 2z"/><circle cx="24" cy="66" r="4"/><circle cx="16" cy="74" r="2.5"/></svg>
    <h3>Dream Act</h3>
    <p>Lorem ipsum dolor sit amet, consectetur adipiscing elit, sed do</p>
    <span class="btn">Read More</span>
  </div>
  <div class="action-card">
    <svg viewBox="0 0 78 78" fill="none" stroke="#d80f0f" stroke-width="2.6" stroke-linecap="round" stroke-linejoin="round"><path d="M14 18l10-10 16 16-10 10z"/><path d="M30 34l14 20 6-3 4 5 6-3 5 6 6-5-9-13-8 2-4-5-6 2-8-13"/><path d="M50 26l6-6M58 34l6-3"/></svg>
    <h3>Worker Rights</h3>
    <p>Lorem ipsum dolor sit amet, consectetur adipiscing elit, sed do</p>
    <span class="btn">Read More</span>
  </div>
</div>

<section class="abs events" role="img" aria-label="Dim photo of rows of crops in a farm field at dusk">
  <h2 class="abs section-title">Upcoming Events</h2>
  <div class="abs event-card" style="left:113px">
    <div class="event-date"><b>30</b><span>OCT 2020</span></div>
    <div class="event-body">
      <h4>Essecntial Farm Work Rpoject</h4>
      <p>Lorem ipsum dolor sit amet, consectetur adipiscing elit, sed do eiusmod tempor incididunt ut labore et dolore magna aliqua.</p>
      <div class="attend"><svg width="12" height="14" viewBox="0 0 12 14" fill="none" stroke="#0f9aa0" stroke-width="1.4"><circle cx="6" cy="4" r="3"/><path d="M1 13c0-3 2-5 5-5s5 2 5 5z"/></svg><span><b>5, 000</b> Attending</span></div>
    </div>
  </div>
  <div class="abs event-card" style="left:607px">
    <div class="event-date"><b>30</b><span>OCT 2020</span></div>
    <div class="event-body">
      <h4>Essecntial Farm Work Rpoject</h4>
      <p>Lorem ipsum dolor sit amet, consectetur adipiscing elit, sed do eiusmod tempor incididunt ut labore et dolore magna aliqua.</p>
      <div class="attend"><svg width="12" height="14" viewBox="0 0 12 14" fill="none" stroke="#0f9aa0" stroke-width="1.4"><circle cx="6" cy="4" r="3"/><path d="M1 13c0-3 2-5 5-5s5 2 5 5z"/></svg><span><b>5, 000</b> Attending</span></div>
    </div>
  </div>
</section>

<h2 class="abs section-title" style="top:2206px">Latest News</h2>
<div class="abs news">
  <div class="news-item photo-farmer" role="img" aria-label="Farmworker holding a tray of harvested cacao pods"></div>
  <div class="news-item news-feature">
    <h4>In Kansas and Missouri, Immigrants are Rooted in the Agriculture Workforce</h4>
    <a href="#">Read more &gt;</a>
  </div>
  <div class="news-item photo-farmer" role="img" aria-label="Farmworker holding a tray of harvested cacao pods"></div>
</div>

<section class="abs support photo-standing" role="img" aria-label="Row of workers standing on dry soil, seen from the knees down">
  <h2 class="abs section-title">Support Our Work</h2>
  <span class="abs btn">Donate</span>
</section>

<h2 class="abs stories-title">Workers and Memebers’ Stories</h2>
<div class="abs quote-mark">“</div>
<p class="abs story-text">Lorem ipsum dolor sit amet, consectetur adipiscing elit, sed do eiusmod tempor incididunt ut labore et dolore magna aliqua. Quis ipsum suspendisse ultrices gravida. Risus commodo viverra maecenas accumsan lacus vel facilisis. Lorem ipsum dolor sit amet, consectetur adipiscing elit, sed do eiusmod tempor incididunt ut labore et dolore magna aliqua. Quis ipsum suspendisse ultrices gravida. Risus commodo viverra maecenas accumsan lacus vel facilisis. Lorem ipsum dolor sit amet, consectetur adipiscing elit, sed do eiusmod tempor incididunt ut labore et dolore magna aliqua. Quis ipsum suspendisse ultrices gravida. Risus commodo viverra maecenas accumsan lacus vel facilisis.</p>
<p class="abs story-author">- John Doe</p>
<div class="abs arrows">
  <span class="arrow"><svg width="8" height="8" viewBox="0 0 8 8" fill="none" stroke="#fff" stroke-width="1.6"><path d="M5 1L2 4l3 3"/></svg></span>
  <span class="arrow"><svg width="8" height="8" viewBox="0 0 8 8" fill="none" stroke="#fff" stroke-width="1.6"><path d="M3 1l3 3-3 3"/></svg></span>
</div>
<div class="abs feed" role="img" aria-label="Social feed of photos: workers standing in a field, crop rows, and farmworkers harvesting">
  <div class="big photo-standing"></div><div class="photo-rows"></div><div class="photo-crop"></div>
  <div class="photo-farmer"></div><div class="photo-field"></div>
  <div class="photo-rows"></div><div class="photo-crop"></div><div class="big photo-standing"></div>
  <div class="photo-farmer"></div><div class="photo-field"></div>
</div>

<footer class="abs footer">
  <a href="#">Join</a><a href="#">Private Policy</a><a href="#">Terms of Services</a><a href="#">Careers</a><a href="#">Contact Us</a><a href="#">Donate Now</a><a href="#">Find us on Social</a>
  <span class="social"><span style="background:#3b5fae"></span><span style="background:#33a4e6"></span></span>
</footer>

</body>
</html>
```